Upmarket building and construction company needs signage

Our building company R Brent Construction, needs signage to put up on the side of our vehicle trailers and on site fencing. We are a building company that specialises in residential construction and carpentry .

I will attach our logo and some inspirational pics for site fencing as well as what our trailer looks like .
Other details i would like on the sign are our
( email) rbrentconstruction@mailbox-example.net
(mobile ) 0493 518 264
(website ) rbrentconstruction. example.net

Target Market(s)

Home owners looking for a reliable local builder who produces good quality work. I have attached some inspirational pics.

Industry/Entity Type

Building and Construction

Colors

Designer to choose colors to be used in the design.

Requirements
Must have
• Our logo, contact information
Nice to have
• We would like the design to have elements of being Elegant, Serious, Modern, Professional, Masculine, Conservative and Upmarket.

```html
<!DOCTYPE html>
<html lang="en">
<head>
<meta charset="utf-8">
<title>R Brent Construction – Site Fence Signage</title>
<link rel="stylesheet" href="https://fonts.googleapis.com/css2?family=Jost:wght@400&display=swap">
<style>
  :root {
    --page: #ffffff;
    --navy: #0b2338;
    --stone: #8c8c8c;
    --font: "Jost", "Futura", sans-serif;
  }
  * { box-sizing: border-box; margin: 0; padding: 0; }
  html, body {
    width: 960px;
    height: 1200px;
    overflow: hidden;
    background: var(--page);
    font-family: var(--font);
  }
  .canvas {
    position: relative;
    width: 960px;
    height: 1200px;
  }
  .sign {
    position: absolute;
    left: 40px;
    top: 377px;
    width: 880px;
    height: 446px;
    background: var(--navy);
    color: var(--stone);
  }
  .brand {
    position: absolute;
    left: 62px;
    top: 150px;
    width: 330px;
  }
  .brand-name {
    font-weight: 400;
    font-size: 44px;
    line-height: 1.05;
    letter-spacing: 0.02em;
    color: var(--stone);
  }
  .brand-tagline {
    margin-top: 14px;
    font-size: 19px;
    letter-spacing: 0.06em;
    text-transform: uppercase;
  }
  .divider {
    position: absolute;
    left: 439px;
    top: 36px;
    width: 2px;
    height: 374px;
    background: var(--stone);
  }
  .contact {
    position: absolute;
    right: 56px;
    top: 172px;
    text-align: right;
    list-style: none;
    font-weight: 400;
  }
  .contact-email { font-size: 19px; letter-spacing: 0.01em; }
  .contact-phone { font-size: 40px; letter-spacing: 0.03em; margin-top: 8px; line-height: 1.1; }
  .contact-web { font-size: 22px; letter-spacing: 0.01em; margin-top: 12px; }
</style>
</head>
<body>
  <main class="canvas">
    <section class="sign" aria-label="R Brent Construction site fence banner">
      <div class="brand">
        <p class="brand-name">R Brent<br>Construction</p>
        <p class="brand-tagline">Building and Carpentry</p>
      </div>
      <div class="divider" aria-hidden="true"></div>
      <ul class="contact">
        <li class="contact-email">rbrentconstruction@mailbox-example.net</li>
        <li class="contact-phone">0493 518 264</li>
        <li class="contact-web">rbrentconstruction. example.net</li>
      </ul>
    </section>
  </main>
</body>
</html>
```